Kestrel Photography Business Card

I need a business card designed for a photography business based in Perth, Western Australia called Kestrel Photography.

We specialise in wedding, event photography and portrait photography.

The business card must borrow the style of the attached logo.

The hex codes for the colours in the logo are:
#ED1D85 - Pink
#89C23E - Green
#37282F - Black

The name on the card will be:
Name: Torvane
Phone: 0417395286
Website: www.kestrelphotography.example.au
Facebook: kestrelphotography

I am open and happy to accept creative concepts.

I’d like some space at the back for writing notes and appointment details.

```html
<!DOCTYPE html>
<html lang="en">
<head>
<meta charset="utf-8">
<title>Kestrel Photography – Business Card</title>
<link rel="stylesheet" href="https://fonts.googleapis.com/css2?family=Questrial&display=swap">
<style>
  :root {
    --pink: #ED1D85;
    --green: #89C23E;
    --ink: #37282F;
    --card-black: #161616;
    --card-white: #ffffff;
    --ring-dark: rgba(120, 120, 120, 0.45);
    --ring-light: rgba(200, 200, 200, 0.55);
    --stage: #ece8e3;
    --text-dark: #111111;
    --text-light: #f2f2f2;
  }
  * { box-sizing: border-box; margin: 0; padding: 0; }
  html, body {
    width: 1200px;
    height: 900px;
    overflow: hidden;
    background: var(--stage);
    font-family: "Questrial", Arial, sans-serif;
  }
  .stage {
    position: relative;
    width: 1200px;
    height: 900px;
  }
  .card {
    position: absolute;
    top: 300px;
    width: 500px;
    height: 290px;
    overflow: hidden;
    box-shadow: 0 6px 18px rgba(0, 0, 0, 0.18);
  }
  .card--front {
    left: 60px;
    background: var(--card-black);
  }
  .card--back {
    left: 640px;
    background: var(--card-white);
  }
  .petal-ring {
    position: absolute;
    border-radius: 50%;
  }
  .card--front .petal-ring {
    left: 20px;
    top: -110px;
    width: 440px;
    height: 440px;
    background: radial-gradient(circle, transparent 0 55%, var(--ring-dark) 58% 70%, transparent 73%);
  }
  .card--back .petal-ring {
    left: 50px;
    top: -60px;
    width: 410px;
    height: 410px;
    background: radial-gradient(circle, transparent 0 58%, var(--ring-light) 61% 72%, transparent 75%);
  }
  .brand-mark {
    position: absolute;
    left: 214px;
    top: 82px;
    width: 82px;
    height: 82px;
    border-radius: 50%;
    background: var(--pink);
  }
  .brand-name {
    position: absolute;
    left: 0;
    right: 0;
    top: 206px;
    text-align: center;
    color: var(--text-light);
    font-size: 17px;
    letter-spacing: 0.42em;
    text-transform: uppercase;
  }
  .contact {
    position: absolute;
    left: 0;
    right: 0;
    top: 46px;
    text-align: center;
    color: var(--text-dark);
    text-transform: uppercase;
    line-height: 22px;
  }
  .contact__name {
    color: var(--pink);
    font-size: 17px;
    letter-spacing: 0.08em;
    font-variant: small-caps;
    text-transform: none;
  }
  .contact__phone {
    font-size: 15px;
    letter-spacing: 0.08em;
  }
  .contact__web,
  .contact__social {
    font-size: 12.5px;
    letter-spacing: 0.1em;
  }
  .contact__social {
    display: flex;
    justify-content: center;
    align-items: center;
    gap: 7px;
  }
  .social-dot {
    width: 14px;
    height: 14px;
    border-radius: 50%;
    background: #666666;
  }
</style>
</head>
<body>
  <main class="stage">
    <section class="card card--front" aria-label="Business card front">
      <div class="petal-ring" role="img" aria-label="Faint ring of grey leaf petals around the brand mark"></div>
      <div class="brand-mark"></div>
      <p class="brand-name">Kestrel Photography</p>
    </section>

    <section class="card card--back" aria-label="Business card back">
      <div class="petal-ring" role="img" aria-label="Faint ring of pale grey leaf petals leaving space for notes"></div>
      <div class="contact">
        <p class="contact__name">Torvane</p>
        <p class="contact__phone">0417395286</p>
        <p class="contact__web">www.kestrelphotography.example.au</p>
        <p class="contact__social"><span class="social-dot"></span>kestrelphotography</p>
      </div>
    </section>
  </main>
</body>
</html>
```